Tech Company Letterhead/Business Cards/Envelopes

We would like a new stationary design for a technology company that develops full turnkey solutions for governments related to Data, Identity Tracking, Fingerprinting, Passport Control, and Border Protection Systems.

We would like the stationary designs to include:

Letter Head
Business Cards
Envelopes

Target Market(s)

Corporate

Industry/Entity Type

Business

Contact Information for Business Card

Details to be shared with the winner.

Font styles to use
Serif
Sans Serif

Colors
e4daeb
85abd2
3176b5
0355a3
0692cd

```html
<!DOCTYPE html>
<html lang="en">
<head>
<meta charset="UTF-8">
<title>Norvex Business Card</title>
<link rel="stylesheet" href="https://fonts.googleapis.com/css2?family=Open+Sans:wght@400;600;700&family=Raleway:wght@500&display=swap">
<style>
  :root {
    --page-bg: #e9ebee;
    --card-white: #ffffff;
    --brand-blue: #0a6fc2;
    --brand-deep: #0355a3;
    --brand-light: #3f8fd0;
    --rule-blue: #3176b5;
    --text-grey: #4a4d52;
    --logo-grey: #6e7175;
    --back-logo: #e6eaef;
  }
  * { margin: 0; padding: 0; box-sizing: border-box; }
  html, body {
    width: 1200px; height: 950px; overflow: hidden;
    background: var(--page-bg);
    font-family: "Open Sans", Arial, sans-serif;
  }
  .stationery {
    position: relative; width: 1200px; height: 950px;
  }
  .card {
    position: absolute; left: 300px; width: 600px; height: 343px;
    border-radius: 4px;
    box-shadow: 0 10px 28px rgba(0,0,0,0.18);
    overflow: hidden;
  }
  /* Back of card */
  .card-back {
    top: 90px;
    background: linear-gradient(135deg, var(--brand-light) 0%, var(--brand-blue) 45%, var(--brand-deep) 100%);
    display: flex; flex-direction: column; align-items: center; justify-content: center;
  }
  .card-back .brand-name {
    font-family: "Raleway", sans-serif; font-weight: 500;
    font-size: 84px; letter-spacing: 10px; color: var(--back-logo);
  }
  .card-back .brand-web {
    margin-top: 8px; font-size: 18px; letter-spacing: 3px; color: var(--back-logo);
  }
  /* Front of card */
  .card-front {
    top: 500px; background: var(--card-white);
  }
  .card-front .brand-name {
    position: absolute; top: 62px; right: 48px;
    font-family: "Raleway", sans-serif; font-weight: 500;
    font-size: 58px; letter-spacing: 7px; color: var(--logo-grey);
  }
  .holder { position: absolute; left: 46px; top: 120px; }
  .holder-name { font-size: 22px; font-weight: 700; color: var(--brand-blue); }
  .holder-role { font-size: 14px; color: var(--text-grey); margin-top: 1px; }
  .divider {
    position: absolute; left: 46px; right: 40px; top: 177px;
    height: 1.5px; background: var(--rule-blue);
  }
  .address {
    position: absolute; left: 46px; top: 192px;
    font-size: 16px; line-height: 24px; color: var(--text-grey);
  }
  .contacts {
    position: absolute; right: 40px; bottom: 30px;
    list-style: none; text-align: right;
  }
  .contacts li {
    display: flex; align-items: center; justify-content: flex-end; gap: 12px;
    font-size: 16px; line-height: 26px; color: var(--text-grey);
  }
  .contacts svg { width: 18px; height: 16px; fill: var(--brand-blue); }
</style>
</head>
<body>
<main class="stationery">
  <section class="card card-back" aria-label="Card back">
    <div class="brand-name">NORVEX</div>
    <div class="brand-web">www.norvex.com</div>
  </section>

  <section class="card card-front" aria-label="Card front">
    <div class="brand-name">NORVEX</div>
    <div class="holder">
      <div class="holder-name">Adam Keller</div>
      <div class="holder-role">President</div>
    </div>
    <div class="divider"></div>
    <address class="address" style="font-style:normal">
      2190 Harlow Avenue<br>
      Brookdale, NY 11420<br>
      www.norvex.com
    </address>
    <ul class="contacts">
      <li>555 0142 7781
        <svg viewBox="0 0 18 16" aria-hidden="true"><path d="M1 5c0-2 3-4 8-4s8 2 8 4v1h-4V4.5C11.5 4 6.5 4 5 4.5V6H1z"/><path d="M4 8l2-1h6l2 1 1 7H3z"/></svg>
      </li>
      <li>555 0198 3306
        <svg viewBox="0 0 18 16" aria-hidden="true"><rect x="4" y="1" width="10" height="4"/><rect x="1" y="6" width="16" height="7" rx="1"/><rect x="4" y="11" width="10" height="4" fill="#fff" stroke="currentColor"/></svg>
      </li>
      <li>adam@norvex.com
        <svg viewBox="0 0 18 16" aria-hidden="true"><path d="M1 3h16v1.2L9 9 1 4.2z"/><path d="M1 6l8 4.8L17 6v7H1z"/></svg>
      </li>
    </ul>
  </section>
</main>
</body>
</html>
```